Velvet Pressings Techno Label Business Card

I'm looking for a very clean business card for my Velvet Pressings music label. The label focusses on techno music. The card should include:

• my name : Bram Quintel as "Founder & CEO"
• email address: bram@velvet-pressings.example
• web: www.velvet-pressings.example
• facebook logo + /velvetpress
• twitter logo + /velvetpress
• soundcloud logo + /velvetpressings

Feel free to include your ideas! I'm looking forward to discuss about it.

Bram

Industry/Entity Type

Business

Contact Information for Business Card

I don't like glossy cards. Prefer matt.

Requirements
Nice to have
• Maybe on one side the complete logo, other side just the icon.
Should not have
• Flashy stuff. Must be clean and business like style.

```html
<!DOCTYPE html>
<html lang="en">
<head>
<meta charset="utf-8">
<title>Velvet Pressings Business Card</title>
<link rel="stylesheet" href="https://fonts.googleapis.com/css2?family=Lato:wght@400;700;900&display=swap">
<style>
  :root {
    --backdrop: #3b3b3b;
    --brand-orange: #f26722;
    --brand-peach: #fcc3a3;
    --brand-grey: #808080;
    --text-grey: #6f6f6f;
    --card-white: #ffffff;
  }
  * { box-sizing: border-box; margin: 0; padding: 0; }
  html, body {
    width: 1200px; height: 1000px; overflow: hidden;
    background: var(--backdrop);
    font-family: "Lato", Arial, sans-serif;
  }
  .canvas { position: relative; width: 1200px; height: 1000px; }
  .card { position: absolute; overflow: hidden; }

  .card--front-orange {
    left: 61px; top: 168px; width: 532px; height: 327px;
    background: var(--brand-orange);
  }
  .card--front-white {
    left: 616px; top: 168px; width: 534px; height: 327px;
    background: var(--card-white);
  }
  .brand-lockup {
    position: absolute; inset: 0;
    display: flex; align-items: center; justify-content: center; gap: 16px;
  }
  .brand-dot { width: 54px; height: 54px; border-radius: 50%; }
  .brand-name { font-weight: 900; font-size: 34px; letter-spacing: -0.3px; }
  .card--front-orange .brand-dot { background: var(--card-white); }
  .card--front-orange .brand-name { color: var(--card-white); }
  .card--front-white .brand-dot { background: var(--brand-orange); }
  .card--front-white .brand-name { color: var(--brand-orange); }

  .card--back {
    left: 327px; top: 516px; width: 556px; height: 342px;
    background: var(--card-white);
  }
  .back-header {
    position: absolute; left: 33px; top: 38px;
    display: flex; align-items: center; gap: 14px;
  }
  .back-header .brand-dot { width: 48px; height: 48px; background: var(--brand-orange); }
  .back-header .brand-name { font-size: 34px; color: var(--brand-orange); }

  .person { position: absolute; left: 32px; top: 128px; }
  .person-name { font-weight: 700; font-size: 21px; color: var(--brand-orange); line-height: 1.2; }
  .person-role { font-size: 14px; color: var(--text-grey); margin-top: 3px; }

  .contact-list { position: absolute; left: 34px; top: 195px; list-style: none; }
  .contact-item {
    display: flex; align-items: center; gap: 9px;
    height: 21px; font-size: 14px; color: var(--text-grey);
  }
  .contact-icon { width: 15px; height: 15px; flex: none; }
  .social-dot { width: 11px; height: 11px; margin: 2px; border-radius: 50%; background: var(--brand-orange); flex: none; }

  .decor-circle {
    position: absolute; left: 400px; top: 173px;
    width: 122px; height: 122px; border-radius: 50%;
    background: var(--brand-peach);
  }
  .footer-band { position: absolute; left: 0; bottom: 0; width: 556px; height: 36px; }
</style>
</head>
<body>
<main class="canvas">

  <section class="card card--front-orange" aria-label="Card front, orange">
    <div class="brand-lockup">
      <span class="brand-dot"></span>
      <span class="brand-name">Velvet Pressings</span>
    </div>
  </section>

  <section class="card card--front-white" aria-label="Card front, white">
    <div class="brand-lockup">
      <span class="brand-dot"></span>
      <span class="brand-name">Velvet Pressings</span>
    </div>
  </section>

  <section class="card card--back" aria-label="Card back with contact details">
    <div class="back-header">
      <span class="brand-dot"></span>
      <span class="brand-name">Velvet Pressings</span>
    </div>

    <div class="person">
      <p class="person-name">Bram Quintel</p>
      <p class="person-role">Founder &amp; CEO</p>
    </div>

    <ul class="contact-list">
      <li class="contact-item">
        <svg class="contact-icon" viewBox="0 0 16 16" aria-hidden="true">
          <rect x="1" y="3" width="14" height="10" fill="var(--brand-orange)"/>
          <path d="M1 3 L8 9 L15 3" fill="none" stroke="#fff" stroke-width="1.4"/>
        </svg>
        bram@velvet-pressings.example
      </li>
      <li class="contact-item">
        <svg class="contact-icon" viewBox="0 0 16 16" aria-hidden="true">
          <circle cx="8" cy="8" r="7" fill="var(--brand-orange)"/>
          <path d="M1 8 H15 M8 1 V15 M8 1 C4 5 4 11 8 15 M8 1 C12 5 12 11 8 15" fill="none" stroke="#fff" stroke-width="1"/>
        </svg>
        www.velvet-pressings.example
      </li>
      <li class="contact-item"><span class="social-dot"></span>/velvetpress</li>
      <li class="contact-item"><span class="social-dot"></span>/velvetpress</li>
      <li class="contact-item"><span class="social-dot"></span>/velvetpressings</li>
    </ul>

    <div class="decor-circle"></div>

    <svg class="footer-band" viewBox="0 0 556 36" aria-hidden="true">
      <rect x="0" y="24" width="556" height="12" fill="var(--brand-orange)"/>
      <rect x="270" y="12" width="286" height="12" fill="var(--brand-grey)"/>
      <path d="M0 0 H264 Q272 0 272 8 V36 H0 Z" fill="var(--brand-orange)"/>
    </svg>
  </section>

</main>
</body>
</html>
```